Premium men's gut health supplement needs a bottle label designed

We’re mossleaf - a premium men’s wellness brand focused on gut health. Our first product is a high-quality daily supplement designed to support digestion, regularity, and internal cleanliness. Backed by science and tailored for modern lifestyles, mossleaf is crafted in the UK and proudly LGBT-owned. It aims to resolve intimacy problems that gay men may experience due to poor digestion but also does not exclude any other orientation - other men may use it simply to improve their digestion.

mossleaf is for health-conscious men who value science-backed supplements and want to feel confident from the inside out. Many of our early adopters will be gay and bisexual men who prioritise gut health as part of their self-care, sexual, and hygiene routine, though the product is equally effective and appealing to anyone seeking premium digestive support.

The product is premium the target customer is male, not specific to one location but primary markets will be US, UK and EU.

I’d like a supplement bottle designed for mossleaf, our premium men’s gut health brand. The focus should be clean, slightly clinical, and minimal - inspired by brands like Varnō and Brek. The key element is the wordmark (mossleaf) on the front, with no additional logo or icon. Lowercase text and a strong, contemporary font are preferred.

The bottle should be aesthetically pleasing so that people are proud to display it on their shelf, instead of hiding it in a cupboard (like Varnō, brek, Ada Penrith, Olvanne etc)

Avoid anything that shows the product as being for LGBT, e.g., no rainbows, men holding hands etc.

The design should be premium, minimalist and not be busy or overwhelming.

I have uploaded a file called "Bottle" to give an idea of the type of container, but please ignore the colours and change as you see fit. This is just for reference for the type of bottle we'll use - all colours are customisable.

I have also uploaded some images for "style" reference, e.g., brek, varno, ada penrith, etc for inspiration.

```html
<!DOCTYPE html>
<html lang="en">
<head>
<meta charset="utf-8">
<title>mossleaf — Gut Health Supplements For Man</title>
<link rel="stylesheet" href="https://fonts.googleapis.com/css2?family=Barlow+Semi+Condensed:wght@400;600&display=swap">
<style>
  :root {
    --backdrop: #7b7b7b;
    --label: #1f1d1e;
    --label-edge: #141314;
    --decor-tone: #2e2c2e;
    --text-light: #e6e4e2;
    --gold: #c0944a;
  }
  * { margin: 0; padding: 0; box-sizing: border-box; }
  html, body {
    width: 1200px;
    height: 829px;
    overflow: hidden;
    background: var(--backdrop);
  }
  .canvas {
    position: relative;
    width: 1200px;
    height: 829px;
    font-family: "Barlow Semi Condensed", "Arial Narrow", sans-serif;
  }
  .label {
    position: absolute;
    left: 300px;
    top: 64px;
    width: 600px;
    height: 700px;
    background: linear-gradient(90deg, var(--label-edge) 0%, var(--label) 18%, var(--label) 82%, var(--label-edge) 100%);
    overflow: hidden;
  }
  .decor-area {
    position: absolute;
    left: 40px;
    top: 150px;
    width: 380px;
    height: 390px;
    background: radial-gradient(ellipse at 50% 50%, var(--decor-tone) 0%, rgba(46, 44, 46, 0.5) 45%, rgba(31, 29, 30, 0) 75%);
  }
  .wordmark {
    position: absolute;
    left: 181px;
    top: 295px;
    width: 630px;
    height: 100px;
    line-height: 100px;
    text-align: center;
    transform: rotate(90deg);
    color: var(--gold);
    font-weight: 600;
    font-size: 96px;
    letter-spacing: 26px;
    text-indent: 26px;
    text-transform: lowercase;
    white-space: nowrap;
  }
  .product-info {
    position: absolute;
    left: 42px;
    top: 552px;
    font-size: 28px;
    font-weight: 400;
    line-height: 41px;
    color: var(--text-light);
  }
  .product-info .accent { color: var(--gold); }
</style>
</head>
<body>
  <main class="canvas">
    <section class="label">
      <div class="decor-area" role="img" aria-label="Large faint decorative emblem in dark grey"></div>
      <div class="wordmark">mossleaf</div>
      <div class="product-info">
        <p class="product-type">Gut Health</p>
        <p class="product-line">Supplements <span class="accent">For Man</span></p>
        <p class="product-count accent">30 Capsules</p>
      </div>
    </section>
  </main>
</body>
</html>
```